Verpackungsdesign für Premium-Nahrungsergänzungsmittel
Zielgruppe
Dr. Nemo Fortal: Premium-Nahrungsergänzungsmittel für Männer über 40. Unsere Marke verkörpert Vitalität, Expertise und Lebensfreude.
Aufgabenstellung
'DR. NEMO FORTAL' ist eine Premium-Marke, die sich auf Nahrungsergänzungsmittel für Männer über 40 spezialisiert hat. Für unser erstes Produkt 'Quorabin' benötigen wir ein Verpackungsdesign, das die Essenz unserer Marke und das Potenzial des Produkts einfängt.
ZIELGRUPPE:
Männer über 40, gesundheitsbewusst und auf der Suche nach qualitativ hochwertigen, natürlich gewonnenen Nahrungsergänzungsmitteln.
UPDATE 23082023: Briefing optimiert und neu hochgeladen

```html
<!DOCTYPE html>
<html lang="de">
<head>
<meta charset="utf-8">
<title>Quorabin – Verpackung</title>
<link rel="stylesheet" href="https://fonts.googleapis.com/css2?family=League+Spartan:wght@700;800&family=Jost:wght@400;500&display=swap">
<style>
  :root {
    --lime: #8cc63f;
    --teal: #00a99d;
    --fold: #9fd155;
    --white: #ffffff;
    --page: #ffffff;
  }
  html, body {
    margin: 0;
    padding: 0;
    width: 1200px;
    height: 1200px;
    overflow: hidden;
    background: var(--page);
  }
  .canvas {
    position: relative;
    width: 1200px;
    height: 1200px;
  }
  .front-panel {
    position: absolute;
    left: 134px;
    top: 56px;
    width: 797px;
    height: 710px;
    background: var(--lime);
    overflow: hidden;
  }
  .flower-motif {
    position: absolute;
    left: -380px;
    top: 58px;
    width: 760px;
    height: 760px;
    border-radius: 50%;
    background: radial-gradient(circle, var(--teal) 0%, rgba(0,169,157,0.75) 45%, rgba(0,169,157,0) 72%);
  }
  .brand-block {
    position: absolute;
    right: 0;
    top: 0;
    width: 337px;
    height: 269px;
    background: var(--teal);
  }
  .base-band {
    position: absolute;
    right: 0;
    bottom: 0;
    width: 337px;
    height: 62px;
    background: var(--teal);
  }
  .fold-line {
    position: absolute;
    left: 0;
    width: 100%;
    height: 1px;
    background: var(--fold);
    opacity: 0.7;
  }
  .fold-line.upper { top: 269px; }
  .fold-line.lower { top: 648px; }
  .brand-mark {
    position: absolute;
    left: 682px;
    top: 150px;
    width: 200px;
    display: flex;
    flex-direction: column;
    align-items: center;
    gap: 10px;
  }
  .brand-mark .dot {
    width: 52px;
    height: 52px;
    border-radius: 50%;
    background: var(--white);
  }
  .brand-mark .brand-name {
    font-family: "Jost", sans-serif;
    font-weight: 500;
    font-size: 17px;
    color: var(--white);
    letter-spacing: 0.5px;
  }
  .product-title {
    position: absolute;
    left: 268px;
    top: 355px;
    margin: 0;
    font-family: "League Spartan", sans-serif;
    font-weight: 800;
    font-size: 124px;
    line-height: 1;
    color: var(--white);
    letter-spacing: -1px;
  }
  .side-panel {
    position: absolute;
    left: 756px;
    width: 284px;
    height: 78px;
    background: var(--teal);
    overflow: hidden;
  }
  .side-panel.top { top: 865px; }
  .side-panel.bottom { top: 962px; }
  .side-panel .flower-motif {
    width: 220px;
    height: 220px;
    left: 30px;
    top: -110px;
    background: radial-gradient(circle, var(--lime) 0%, rgba(140,198,63,0.7) 40%, rgba(140,198,63,0) 70%);
  }
  .side-panel.bottom .flower-motif { top: 10px; }
  .side-panel .side-title {
    position: absolute;
    right: 10px;
    top: 26px;
    margin: 0;
    font-family: "League Spartan", sans-serif;
    font-weight: 800;
    font-size: 34px;
    line-height: 1;
    color: var(--white);
  }
  .side-panel .side-dot {
    position: absolute;
    right: 10px;
    bottom: 8px;
    width: 16px;
    height: 16px;
    border-radius: 50%;
    background: var(--white);
  }
</style>
</head>
<body>
<div class="canvas">
  <section class="front-panel">
    <div class="flower-motif" role="img" aria-label="Große stilisierte Blüte mit türkisen Blütenblättern"></div>
    <div class="brand-block"></div>
    <div class="base-band"></div>
    <div class="fold-line upper"></div>
    <div class="fold-line lower"></div>
  </section>

  <div class="brand-mark">
    <span class="dot"></span>
    <span class="brand-name">Dr. Nemo Fortal</span>
  </div>

  <h1 class="product-title">QUORABIN</h1>

  <section class="side-panel top">
    <div class="flower-motif" role="img" aria-label="Stilisierte Blüte in Hellgrün"></div>
    <p class="side-title">QUORABIN</p>
  </section>

  <section class="side-panel bottom">
    <div class="flower-motif" role="img" aria-label="Stilisierte Blüte in Hellgrün"></div>
    <span class="side-dot"></span>
  </section>
</div>
</body>
</html>
```